Amber Kite Photography

Wanting to get up a photography website.

Want it to include a portfolio section but also want to be able to issue client passwords for particular event so they are able to view and then click on a photo to buy the unwatermarked version etc.

Ppen to suggestions and different ideas.

Looking for an HTML version and will pay more to get it up online.

• a link to my FB page

```html
<!DOCTYPE html>
<html lang="en">
<head>
<meta charset="utf-8">
<title>Amber Kite Photography</title>
<link rel="stylesheet" href="https://fonts.googleapis.com/css2?family=Arimo:wght@400;700&display=swap">
<style>
  :root {
    --ink: #1a1a1a;
    --text: #2b2b2b;
    --muted: #8a8a8a;
    --social: #7d7d7d;
    --white: #ffffff;
    --red: #d0141a;
    --frame: #bdbdbd;
    --rule: #cfcfcf;
  }
  * { box-sizing: border-box; margin: 0; padding: 0; }
  html, body {
    width: 1200px; height: 960px; overflow: hidden;
    background: var(--white);
    font-family: "Arimo", Arial, sans-serif;
    color: var(--text);
  }
  .page { position: relative; width: 1200px; height: 960px; }

  /* Hero */
  .hero {
    position: absolute; left: 0; top: 0; width: 1200px; height: 593px;
    background: #060606; overflow: hidden;
  }
  .hero-photo {
    position: absolute; inset: 0;
    background:
      radial-gradient(ellipse 170px 210px at 660px 300px, rgba(235,235,235,0.95) 0%, rgba(205,205,205,0.75) 45%, rgba(150,150,150,0) 100%),
      radial-gradient(ellipse 150px 260px at 500px 170px, rgba(200,200,200,0.55) 0%, rgba(120,120,120,0) 100%),
      radial-gradient(ellipse 140px 120px at 640px 40px, rgba(220,220,220,0.6) 0%, rgba(120,120,120,0) 100%),
      radial-gradient(ellipse 120px 300px at 860px 300px, rgba(170,170,170,0.55) 0%, rgba(90,90,90,0) 100%),
      radial-gradient(ellipse 360px 420px at 640px 320px, #8a8a8a 0%, #4a4a4a 55%, rgba(20,20,20,0) 100%),
      linear-gradient(90deg, #030303 0%, #141414 22%, #3a3a3a 42%, #4a4a4a 62%, #1c1c1c 80%, #050505 100%);
  }
  .top-nav a, .account-nav a {
    position: absolute; top: 17px;
    font-size: 13px; color: var(--white); text-decoration: none; letter-spacing: 0.2px;
  }
  .top-nav a.active { font-weight: 700; }
  .top-nav a.active::after, .category-nav a.active::after {
    content: ""; position: absolute; left: 50%; margin-left: -5px; bottom: -10px;
    border-left: 5px solid transparent; border-right: 5px solid transparent; border-top: 5px solid var(--red);
  }
  .cart {
    position: absolute; left: 850px; top: 46px; width: 150px; height: 39px;
    border: 3px solid #7a7a7a; border-radius: 4px; background: #3c3c3c;
    display: flex; align-items: center; padding-left: 18px; gap: 8px;
    color: var(--white); font-size: 16px; text-decoration: none;
  }
  .cart-count {
    position: absolute; right: 6px; top: 7px; width: 24px; height: 20px;
    background: var(--red); border-radius: 2px; font-size: 12px;
    display: flex; align-items: center; justify-content: center;
  }
  .brand {
    position: absolute; left: 208px; top: 368px;
    color: var(--white); font-size: 40px; font-weight: 400; line-height: 1;
  }
  .brand-sub { display: block; font-size: 11px; letter-spacing: 16.5px; margin-top: 12px; margin-left: 4px; }
  .get-image {
    position: absolute; left: 872px; top: 396px;
    color: #e0e0e0; font-size: 16px; text-decoration: none;
    display: flex; align-items: center; gap: 8px;
  }
  .category-band {
    position: absolute; left: 0; top: 518px; width: 1200px; height: 75px;
    background: linear-gradient(90deg, rgba(5,5,5,0.95) 0%, rgba(10,10,10,0.9) 12%, rgba(40,40,40,0.55) 40%, rgba(40,40,40,0.5) 60%, rgba(10,10,10,0.85) 80%, rgba(5,5,5,0.95) 100%);
  }
  .category-nav a {
    position: absolute; top: 30px;
    color: var(--white); font-size: 16px; letter-spacing: 1.5px; text-decoration: none;
  }

  /* Gallery strip */
  .gallery { position: absolute; left: 0; top: 619px; width: 1200px; height: 82px; }
  .thumb {
    position: absolute; top: 0; width: 124px; height: 81px;
    border: 1px solid var(--frame); background: var(--white); padding: 3px;
  }
  .thumb.current { border: 3px solid var(--ink); padding: 1px; }
  .thumb-photo { width: 100%; height: 100%; }
  .tone-1 { background: radial-gradient(ellipse 45px 35px at 60% 55%, #e6e6e6, #a8a8a8 50%, rgba(40,40,40,0) 100%), linear-gradient(135deg, #0c0c0c 0%, #3a3a3a 45%, #d8d8d8 100%); }
  .tone-2 { background: radial-gradient(ellipse 40px 40px at 50% 50%, #b5b5b5, #5a5a5a 55%, rgba(20,20,20,0) 100%), linear-gradient(90deg, #0a0a0a, #2a2a2a 50%, #0c0c0c); }
  .tone-3 { background: radial-gradient(ellipse 40px 38px at 55% 55%, #dedede, #8e8e8e 55%, rgba(40,40,40,0) 100%), linear-gradient(90deg, #1a1a1a, #6a6a6a 45%, #c4c4c4 80%, #5a5a5a); }
  .tone-4 { background: radial-gradient(ellipse 50px 40px at 50% 55%, #d0d0d0, #9a9a9a 55%, rgba(80,80,80,0) 100%), linear-gradient(180deg, #8a8a8a, #b4b4b4 50%, #707070); }
  .tone-5 { background: radial-gradient(ellipse 40px 30px at 30% 35%, #9a9a9a, rgba(40,40,40,0) 100%), radial-gradient(ellipse 40px 30px at 72% 35%, #8e8e8e, rgba(40,40,40,0) 100%), linear-gradient(180deg, #3a3a3a, #6a6a6a 50%, #1e1e1e); }
  .tone-6 { background: radial-gradient(ellipse 42px 38px at 55% 55%, #c8c8c8, #8a8a8a 55%, rgba(50,50,50,0) 100%), linear-gradient(90deg, #2a2a2a, #6a6a6a 30%, #9a9a9a 70%, #3a3a3a); }
  .gallery-arrow { position: absolute; top: 26px; }
  .shelf-shadow {
    position: absolute; left: 270px; top: 728px; width: 640px; height: 14px;
    background: radial-gradient(ellipse 50% 100% at 50% 0%, rgba(0,0,0,0.12), rgba(0,0,0,0));
  }

  /* Welcome */
  .welcome { position: absolute; left: 202px; top: 767px; width: 420px; }
  .welcome h1 { font-size: 16px; font-weight: 400; color: var(--ink); margin-bottom: 14px; }
  .welcome p { font-size: 12px; line-height: 16px; color: var(--ink); }
  .social-link {
    position: absolute; left: 809px; top: 797px;
    display: flex; align-items: center; gap: 12px; text-decoration: none; color: var(--social);
  }
  .social-dot { width: 47px; height: 47px; border-radius: 50%; background: var(--social); margin-top: 10px; }
  .social-text { display: flex; flex-direction: column; line-height: 1; }
  .social-lead { font-size: 17px; font-weight: 400; color: #9a9a9a; margin-bottom: 6px; }
  .social-name { font-size: 30px; font-weight: 700; letter-spacing: -0.5px; }

  /* Footer */
  .footer-rule { position: absolute; left: 0; top: 922px; width: 1200px; height: 4px; background: var(--rule); }
  .copyright { position: absolute; left: 198px; top: 936px; font-size: 10.5px; color: var(--muted); }
</style>
</head>
<body>
<div class="page">
  <header class="hero">
    <div class="hero-photo" role="img" aria-label="Black and white close-up portrait photograph of a smiling young woman"></div>

    <nav class="top-nav">
      <a class="active" href="#" style="left:199px">HOME</a>
      <a href="#" style="left:273px">ABOUT</a>
      <a href="#" style="left:340px">CONTACT US</a>
      <a href="#" style="left:454px">HELP</a>
    </nav>
    <nav class="account-nav">
      <a href="#" style="left:854px">SIGN IN</a>
      <a href="#" style="left:937px">REGISTER</a>
    </nav>

    <a class="cart" href="#">
      <svg width="26" height="18" viewBox="0 0 26 18" aria-hidden="true">
        <path d="M1 2h4l3 10h13l3-8H7" fill="none" stroke="#fff" stroke-width="2"/>
        <circle cx="10" cy="16" r="1.6" fill="#fff"/><circle cx="19" cy="16" r="1.6" fill="#fff"/>
      </svg>
      <span>Cart</span>
      <span class="cart-count">0</span>
    </a>

    <div class="brand">Amber Kite<span class="brand-sub">PHOTOGRAPHY</span></div>

    <a class="get-image" href="#">GET IMAGE
      <svg width="24" height="16" viewBox="0 0 24 16" aria-hidden="true">
        <path d="M2 1l7 7-7 7M12 1l7 7-7 7" fill="none" stroke="#d0141a" stroke-width="3"/>
      </svg>
    </a>

    <div class="category-band">
      <nav class="category-nav">
        <a class="active" href="#" style="left:211px">PORTRAITS</a>
        <a href="#" style="left:366px">FASHION</a>
        <a href="#" style="left:516px">TRAVEL</a>
        <a href="#" style="left:635px">COMMERCIAL</a>
        <a href="#" style="left:804px">UNIQUE</a>
        <a href="#" style="left:965px">ART</a>
      </nav>
    </div>
  </header>

  <section class="gallery">
    <svg class="gallery-arrow" style="left:76px" width="20" height="30" viewBox="0 0 20 30" aria-hidden="true">
      <path d="M16 3L5 15l11 12" fill="none" stroke="#bdbdbd" stroke-width="4"/>
    </svg>
    <div class="thumb" style="left:198px"><div class="thumb-photo tone-1" role="img" aria-label="Portrait of a young woman resting her head"></div></div>
    <div class="thumb" style="left:335px"><div class="thumb-photo tone-2" role="img" aria-label="Portrait of a young man"></div></div>
    <div class="thumb current" style="left:472px"><div class="thumb-photo tone-3" role="img" aria-label="Portrait of a smiling woman"></div></div>
    <div class="thumb" style="left:608px"><div class="thumb-photo tone-4" role="img" aria-label="Portrait of a blonde woman"></div></div>
    <div class="thumb" style="left:744px"><div class="thumb-photo tone-5" role="img" aria-label="Close-up portrait of a man"></div></div>
    <div class="thumb" style="left:881px"><div class="thumb-photo tone-6" role="img" aria-label="Portrait of a mature woman"></div></div>
    <svg class="gallery-arrow" style="left:1090px" width="20" height="30" viewBox="0 0 20 30" aria-hidden="true">
      <path d="M4 3l11 12L4 27" fill="none" stroke="#bdbdbd" stroke-width="4"/>
    </svg>
  </section>
  <div class="shelf-shadow"></div>

  <section class="welcome">
    <h1>Welcome to Amber Kite !</h1>
    <p>Lorem Ipsum is simply dummy text of the printing and typesetting industry. Lorem Ipsum has been the industry's standard dummy text ever since the 1500s, when an unknown printer took a galley of type and scrambled it to make a type specimen book. It has survived not only five centuries, but also the leap into electronic typesetting, remaining essentially unchanged. It was</p>
  </section>

  <a class="social-link" href="#">
    <span class="social-dot"></span>
    <span class="social-text">
      <span class="social-lead">Visit us on</span>
      <span class="social-name">Friendbook</span>
    </span>
  </a>

  <footer>
    <div class="footer-rule"></div>
    <p class="copyright">© 2013 AmberKite. All rights reserved.</p>
  </footer>
</div>
</body>
</html>
```